Health Benefits Association Website Design

The Allied Household Provision Association (AHPA) is an organization formed for the purpose of providing its members better value for selected health benefits and services. Members can use the association benefits either in conjunction with or independently of other medical insurance they may have. Some of the benefits available include discounted dental and vision care and prescription mail order services. There is no limitation on who can join. This membership will be primarily marketed as a way to enhance the value of a fixed benefit health insurance plan although members do not have to have the insurance plan join the association.

We are seeking a design for a website to be used for consumers to get information about membership and for current members to be able to access their benefits. The website should include:

1) A landing page to provide a description of the AHPA

2) A secondary page that can be duplicated that will:
a. Provide a list of benefits
b. Provide a membership enrollment form
c. Provide a member’s only access page
d. Provide a contact page for more information

We are seeking a modern but conservative design that will reflect value, simplicity and good health. The site design will also need to be compatible for use with mobile phones and tablets.

A copy of the association logo is included with the submission. It will also need to be incorporated into the website design. Layouts of similar association websites have also been included for reference.

Target Market(s)

Ages 25 to 65 unmarried, married with no children, professionals, self-employed, active and healthy

Industry/Entity Type

Health And Wellness

Number of Pages Required

2 page

Font styles to use
Sans Serif

Colors

Designer to choose colors to be used in the design.

Requirements
Must have
• AHPA Logo (attached). Use colors from the logo in the website design.
Nice to have
• Graphics, if used, should convey health and fitness and skew toward a diverse array of adults 25 to 40.

```html
<!DOCTYPE html>
<html lang="en">
<head>
<meta charset="utf-8">
<title>Allied Household Provision Association</title>
<link href="https://fonts.googleapis.com/css2?family=Open+Sans:wght@400;600;700&family=Yellowtail&display=swap" rel="stylesheet">
<style>
:root{
  --olive:#8e9a4b;
  --gold:#fcc815;
  --ink:#222;
  --text:#444;
  --footer:#232323;
  --footer-line:#555;
  --white:#fff;
}
*{margin:0;padding:0;box-sizing:border-box}
html,body{width:820px;height:1200px;overflow:hidden}
body{position:relative;background:var(--white);font-family:'Open Sans',sans-serif;color:var(--text)}
.abs{position:absolute}
.top-bar{left:0;top:0;width:820px;height:56px}
.member-login{right:92px;top:27px;font-size:8px;color:#333;display:flex;align-items:center;gap:6px}
.nav-band{left:0;top:56px;width:820px;height:39px;background:var(--olive)}
.nav{right:80px;top:69px;display:flex;gap:27px;font-size:11.5px;color:var(--white)}
.nav .active{font-weight:700}
.submenu{left:511px;top:95px;width:116px;height:28px;background:var(--gold);font-size:7.5px;color:#333;display:flex;align-items:center;padding-left:15px}
.submenu::before{content:"";position:absolute;left:54px;top:-5px;border:5px solid transparent;border-top:0;border-bottom-color:var(--gold)}
.brand-box{left:68px;top:0;width:127px;height:148px;background:#fafafa;border:1px solid #e2d28a;border-top:0;display:flex;flex-direction:column;align-items:center;justify-content:center;gap:8px;text-align:center;z-index:2}
.brand-mark{width:14px;height:14px;background:var(--olive)}
.brand-name{font-size:10.5px;font-weight:700;color:var(--olive);line-height:1.25;padding:0 8px}
.hero{left:0;top:95px;width:820px;height:342px;background:linear-gradient(100deg,#a87a4c 0%,#c49a62 30%,#6e5a45 55%,#3b4452 70%,#8aa070 100%)}
.hero-title{left:89px;top:228px;font-size:20px;font-weight:700;color:var(--gold);line-height:25px;letter-spacing:.3px}
.hero-btn{left:89px;top:289px;width:85px;height:20px;background:var(--gold);color:#222;font-size:9px;font-weight:700;display:flex;align-items:center;justify-content:center}
.welcome{left:0;top:458px;width:820px;text-align:center}
.welcome h1{font-size:16px;font-weight:700;color:var(--ink);letter-spacing:.5px}
.welcome .rule{width:41px;height:2px;background:var(--olive);margin:7px auto 0}
.welcome-copy{left:110px;top:495px;width:600px;text-align:center;font-size:8px;line-height:14px;color:#555}
.welcome-copy p{margin-bottom:14px}
.signature{left:0;top:643px;width:820px;display:flex;justify-content:center;align-items:center;gap:10px}
.signature .line{width:36px;height:1px;background:var(--olive)}
.signature .name{font-family:'Yellowtail',cursive;font-size:19px;color:var(--olive)}
.sig-role{left:0;top:668px;width:820px;text-align:center;font-size:9px;color:#333}
.card{top:706px;width:208px;height:179px;border:1px solid #ddd;background:var(--white)}
.card .photo{height:105px}
.card h3{font-size:10px;font-weight:400;color:#333;margin:9px 0 0 14px}
.card p{font-size:7.5px;font-weight:600;color:#555;line-height:14px;margin:3px 14px 0}
.enroll-btn{left:168px;top:926px;width:154px;height:38px;background:var(--gold);color:#333;font-size:18px;display:flex;align-items:center;justify-content:center}
.enroll-text{left:341px;top:937px;font-size:13.5px;color:#333}
.footer{left:0;top:994px;width:820px;height:206px}
.footer-about{left:67px;top:1024px;width:150px}
.footer-mark{display:flex;align-items:center;gap:6px;color:var(--gold);font-size:10px;font-weight:700;margin-bottom:12px;line-height:1.3}
.footer-mark span.sq{width:12px;height:12px;background:var(--gold);flex:none}
.footer-about p{font-size:8px;line-height:14px;color:var(--white)}
.f-head{font-size:14px;color:var(--gold);top:1037px}
.links{left:264px;top:1062px;width:110px;font-size:8.5px;color:#ccc}
.links li{list-style:none;height:28px;display:flex;align-items:center;gap:10px;border-bottom:1px dashed var(--footer-line);padding-left:3px}
.testi-arrows{left:533px;top:1039px;display:flex;gap:2px}
.testi-arrows span{width:11px;height:10px;background:#999;display:block}
.avatar{left:408px;top:1061px;width:38px;height:38px;border-radius:50%;background:radial-gradient(circle,#d9d9d9,#8a8a8a);border:2px solid #eee}
.t-name{left:457px;top:1063px;font-size:9.5px;font-weight:700;color:var(--gold)}
.t-role{left:457px;top:1078px;font-size:7.5px;font-style:italic;color:var(--gold)}
.t-quote{left:406px;top:1103px;width:152px;font-size:7.5px;line-height:14px;color:#bbb;text-align:justify}
.contact{left:602px;top:1062px;width:140px;font-size:7.5px;color:#ccc;letter-spacing:.4px}
.contact div{border-bottom:1px dashed var(--footer-line);padding:3px 0 6px;line-height:14px}
.contact div+div{padding-top:8px}
.bottom-line{left:0;top:1173px;width:820px;height:1px;background:#3a3a3a}
.copyright{left:0;top:1181px;width:820px;text-align:center;font-size:7.5px;color:#aaa}
.page-code{right:50px;top:1181px;font-size:7.5px;color:#888}
</style>
</head>
<body>
  <header>
    <div class="abs top-bar"></div>
    <div class="abs member-login">
      <svg width="8" height="9" viewBox="0 0 8 9"><circle cx="4" cy="2.6" r="2" fill="none" stroke="#333"/><path d="M0.8 8.5v-1.5a3.2 3 0 0 1 6.4 0v1.5z" fill="none" stroke="#333"/></svg>
      MEMBER LOGIN
    </div>
    <div class="abs nav-band"></div>
    <nav class="abs nav">
      <span class="active">Home</span><span>Benefits</span><span>Newsletter</span><span>Join</span><span>Contact</span>
    </nav>
    <div class="abs submenu">›&nbsp;&nbsp;HEALTH PROTECTION</div>
    <div class="abs brand-box">
      <div class="brand-mark"></div>
      <div class="brand-name">Allied Household Provision Association</div>
    </div>
  </header>

  <section>
    <div class="abs hero" role="img" aria-label="Smiling couple outdoors, woman on man's back, autumn trees behind"></div>
    <h2 class="abs hero-title">WORKING TO GIVE<br>CONSUMERS AN ADVANTAGE</h2>
    <div class="abs hero-btn">LEARN MORE</div>
  </section>

  <section>
    <div class="abs welcome"><h1>WELCOME</h1><div class="rule"></div></div>
    <div class="abs welcome-copy">
      <p>The Allied Household Provision Association (AHPA) is a non-profit corporation created to improve the well-being of its members. We do this by using our collective purchasing power to obtain discounts on products and services that benefit our members. These include a wide variety of health, consumer, business and travel related benefits.Our goal is not only to provide packages of benefits that provide value to our members, but also to ensure that these benefits are easy to access and use.</p>
      <p>If you are already a member, you may log in to view the great benefits available to you and instructions on how to access them. If this is your first visit to our website as a member, please follow the instructions in your welcome letter to register.</p>
      <p>If you are not currently a member, you may select “Join” on the menu bar and enroll today in order to gain access to these valuable benefits. Thank you for visiting our site. We truly appreciate your membership and look forward to serving you.</p>
    </div>
    <div class="abs signature"><span class="line"></span><span class="name">Rob Kessler</span><span class="line"></span></div>
    <div class="abs sig-role">President</div>
  </section>

  <section>
    <article class="abs card" style="left:67px">
      <div class="photo" role="img" aria-label="Smiling doctor with stethoscope, colleagues behind" style="background:linear-gradient(90deg,#dfe6ec,#f3f5f7 60%,#e8ecef)"></div>
      <h3>Health</h3>
      <p>Neque porro quisquam est, qui dolorem ipsum quia dolor sit amet, consectetur,</p>
    </article>
    <article class="abs card" style="left:295px">
      <div class="photo" role="img" aria-label="Group of diverse young friends laughing together" style="background:linear-gradient(90deg,#6b5a3e,#a3785a 50%,#5d4a3a)"></div>
      <h3>Consumer</h3>
      <p>Neque porro quisquam est, qui dolorem ipsum quia dolor sit amet, consectetur,</p>
    </article>
    <article class="abs card" style="left:522px">
      <div class="photo" role="img" aria-label="Two businessmen reviewing a tablet in an office" style="background:linear-gradient(90deg,#d6d8dc,#8a95a8 50%,#b8c3d1)"></div>
      <h3>Business</h3>
      <p>Neque porro quisquam est, qui dolorem ipsum quia dolor sit amet, consectetur,</p>
    </article>
  </section>

  <section>
    <div class="abs enroll-btn">Enroll Today</div>
    <div class="abs enroll-text">Membership Request to Join items here</div>
  </section>

  <footer>
    <svg class="abs footer" width="820" height="206" viewBox="0 0 820 206"><path d="M0 0Q410 40 820 0V206H0Z" fill="var(--footer)"/></svg>
    <div class="abs footer-about">
      <div class="footer-mark"><span class="sq"></span>Allied Household Provision Association</div>
      <p>The Allied Household Provision Association (AHPA) is a non-profit corporation created to improve the well-being of its members.</p>
    </div>
    <div class="abs f-head" style="left:265px">Usefull Links</div>
    <ul class="abs links">
      <li>›<span>Privacy Policy</span></li>
      <li>›<span>Terms &amp; Conditions</span></li>
      <li>›<span>Sitemap</span></li>
    </ul>
    <div class="abs f-head" style="left:406px">Testimonials</div>
    <div class="abs testi-arrows"><span></span><span></span></div>
    <div class="abs avatar" role="img" aria-label="Portrait of reviewer"></div>
    <div class="abs t-name">Marek Holden</div>
    <div class="abs t-role">CEO</div>
    <p class="abs t-quote">Lorem ipsum dolor sit amet, consectetur adipiscing elit, sed do eiusmod tempor incididunt ut labore et...</p>
    <div class="abs f-head" style="left:589px">Contact</div>
    <div class="abs contact">
      <div>48 Linden Court, Area, City,<br>Country, Zipcode.</div>
      <div>+ 12 (34) 555 0147</div>
      <div style="border:0">info@householdprovision.org</div>
    </div>
    <div class="abs bottom-line"></div>
    <div class="abs copyright">Copyright © 2017 www.householdprovision.org &nbsp;|&nbsp; All Rights Reserved.</div>
    <div class="abs page-code">M1</div>
  </footer>
</body>
</html>
```